Webpage

I am a professional genealogist. I need a webpage that is professional looking (using the logo I chose), I can add hyperlinks and photos to if and when I want.

```html
<!DOCTYPE html>
<html lang="en">
<head>
<meta charset="utf-8">
<title>Whitford Research Services</title>
<link rel="stylesheet" href="https://fonts.googleapis.com/css2?family=Arimo:ital,wght@0,400;0,700;1,400&family=Roboto+Condensed:wght@700&display=swap">
<style>
:root{
  --green:#3aa886;
  --green-text:#2a9474;
  --green-dark:#258a6b;
  --ink:#222;
  --body:#555;
  --white:#fff;
}
*{box-sizing:border-box;margin:0;padding:0}
html,body{width:807px;height:1200px;overflow:hidden;background:var(--white)}
body{font-family:"Arimo",Arial,sans-serif;color:var(--body)}
.page{position:relative;width:807px;height:1200px;overflow:hidden}
.abs{position:absolute}
.topbar{left:0;top:0;width:807px;height:21px;background:var(--green);color:var(--white);font-size:8px;display:flex;align-items:center;justify-content:flex-end;padding-right:117px;gap:16px;white-space:nowrap}
.topbar span{display:flex;align-items:center;gap:4px}
.header{left:0;top:21px;width:807px;height:61px;background:var(--white)}
.brand{left:116px;top:10px;height:40px;display:flex;align-items:center;gap:7px}
.brand-dot{width:40px;height:40px;border-radius:50%;background:var(--green);flex:none}
.brand-name{width:100px;font-size:10px;line-height:11px;color:var(--ink)}
.nav{left:295px;top:0;width:395px;height:61px;display:flex;justify-content:space-between;align-items:center;list-style:none;font-size:8px;color:var(--ink)}
.hero{left:0;top:82px;width:807px;height:300px;background:linear-gradient(90deg,#d9d2c8 0%,#efe9e0 30%,#e6e2dc 55%,#f0eeea 100%)}
.hero-arrow{top:130px;width:29px;height:29px}
.hero-title{left:403px;top:106px;font-family:"Roboto Condensed",Arial,sans-serif;font-weight:700;font-size:23px;color:var(--green-text);letter-spacing:.2px;white-space:nowrap}
.hero-sub{left:403px;top:144px;font-size:13px;color:#111}
.hero-body{left:403px;top:171px;font-size:11.5px;line-height:20px;color:#111}
.section-title{width:807px;text-align:center;font-size:14px;color:var(--green-text)}
.intro{left:144px;top:433px;width:519px;text-align:center;font-size:7.5px;line-height:16px}
.service-img{top:501px;width:131px;height:111px}
.service-name{top:623px;font-size:8.5px;color:var(--green-text)}
.service-desc{top:639px;width:125px;font-size:6.6px;line-height:14.5px;padding-left:1px}
.pub-img{left:115px;top:711px;width:179px;height:134px;background:linear-gradient(90deg,#bfb9b2,#e8e4dd 50%,#c9bfb4)}
.pub-title{left:321px;top:711px;font-size:12px;color:var(--green-text)}
.pub-text{left:321px;top:733px;width:360px;font-size:6.6px;line-height:14.6px}
.btn{left:323px;top:812px;height:25px;display:flex;background:var(--green);color:var(--white);font-size:7px}
.btn-label{width:66px;display:flex;align-items:center;justify-content:center}
.btn-arrow{width:20px;border-left:1px solid rgba(255,255,255,.7);display:flex;align-items:center;justify-content:center}
.posts{left:0;top:882px;width:807px;height:249px;background:var(--green)}
.posts .section-title{top:28px;color:var(--white);font-weight:700;font-size:12px;position:absolute}
.post-img{top:63px;width:176px;height:120px}
.post-title{top:193px;width:176px;text-align:center;color:var(--white);font-size:9.5px;white-space:nowrap}
.post-date{top:208px;width:176px;text-align:center;color:var(--white);font-size:6.5px;font-style:italic}
.posts-arrow{top:120px}
.footer{left:0;top:1131px;width:807px;height:69px;background:var(--green-dark);color:var(--white)}
.footer-nav{left:116px;top:21px;display:flex;list-style:none;font-size:7px}
.copy{left:116px;top:40px;font-size:7px}
.social{left:600px;top:24px;display:flex;gap:6px}
.social span{width:18px;height:18px;border-radius:50%;background:var(--white)}
</style>
</head>
<body>
<div class="page">
  <div class="abs topbar">
    <span>Dana Whitford, Professional Genealogist, PO Box 5500, Cedar Falls, TX 70000-0000.</span>
    <span><svg width="10" height="8" viewBox="0 0 10 8"><path d="M1 3 Q5 0 9 3 L8 4 L6.5 3.2 L6.5 2.5 Q5 2 3.5 2.5 L3.5 3.2 L2 4 Z M2.5 4.5 H7.5 L8.5 7.5 H1.5 Z" fill="#fff"/></svg>Phone : 555-010-2468</span>
    <span><svg width="9" height="7" viewBox="0 0 9 7"><rect x="0" y="0" width="9" height="7" fill="#fff"/><path d="M0 0 L4.5 4 L9 0" fill="none" stroke="#3aa886" stroke-width="1"/></svg>Email : dwhitford@example.net</span>
  </div>

  <header class="abs header">
    <div class="abs brand"><span class="brand-dot"></span><span class="brand-name">Whitford Research Services</span></div>
    <ul class="abs nav">
      <li>Home</li><li>About</li><li>Services</li><li>Contact</li><li>Publications</li><li>Blog</li><li>Links</li>
    </ul>
  </header>

  <section class="abs hero" role="img" aria-label="Photo of a smiling professional man in a suit with colleagues behind">
    <svg class="abs hero-arrow" style="left:52px" viewBox="0 0 29 29"><circle cx="14.5" cy="14.5" r="13" fill="none" stroke="#7fcfb3" stroke-width="1.5" opacity=".8"/><path d="M17 8 L10 14.5 L17 21 Z" fill="#7fcfb3" opacity=".8"/></svg>
    <svg class="abs hero-arrow" style="left:731px" viewBox="0 0 29 29"><circle cx="14.5" cy="14.5" r="13" fill="none" stroke="#7fcfb3" stroke-width="1.5" opacity=".8"/><path d="M12 8 L19 14.5 L12 21 Z" fill="#7fcfb3" opacity=".8"/></svg>
    <div class="abs hero-title">WHITFORD RESEARCH SERVICES</div>
    <div class="abs hero-sub">I PROVIDE THESE SERVICES</div>
    <div class="abs hero-body">Forensic genealogy, kinship determination,<br>research analysis and consultation</div>
  </section>

  <h2 class="abs section-title" style="top:406px;font-weight:400">OUR SERVICES</h2>
  <p class="abs intro">It is a long established fact that a reader will be distracted by the readable content of a page when looking at its layout. The point of using Lorem Ipsum is that it has a more-or-less normal distribution of letters, as opposed to using 'Content here, content here', making it look like readable English. Many desktop publishing packages...</p>

  <div class="abs service-img" style="left:115px;background:linear-gradient(180deg,#6cc2a4,#4aae8d)" role="img" aria-label="Classical columns of a courthouse"></div>
  <svg class="abs" style="left:170px;top:546px" width="21" height="21" viewBox="0 0 21 21"><circle cx="10.5" cy="10.5" r="10" fill="#fff" opacity=".85"/><g fill="none" stroke="#777" stroke-width="1.5"><rect x="6" y="9" width="6" height="3.5" rx="1.7" transform="rotate(-45 9 10.7)"/><rect x="9" y="8.5" width="6" height="3.5" rx="1.7" transform="rotate(-45 12 10.2)"/></g></svg>
  <div class="abs service-img" style="left:263px;background:linear-gradient(180deg,#8a3a22,#5a2414)" role="img" aria-label="Statue of justice holding scales"></div>
  <div class="abs service-img" style="left:411px;background:linear-gradient(135deg,#e8d8c0,#8a5a2c)" role="img" aria-label="Hand writing with a pen beside glasses"></div>
  <div class="abs service-img" style="left:561px;background:linear-gradient(135deg,#6a5a4c,#e8d8c8)" role="img" aria-label="Consultant meeting with a client"></div>

  <div class="abs service-name" style="left:116px">Forensic genealogy</div>
  <div class="abs service-name" style="left:264px">kinship determination</div>
  <div class="abs service-name" style="left:412px">Research analysis</div>
  <div class="abs service-name" style="left:562px">Consultation</div>
  <p class="abs service-desc" style="left:116px">Uncover many web sites still in their infancy various versions...</p>
  <p class="abs service-desc" style="left:264px">Uncover many web sites still in their infancy various versions...</p>
  <p class="abs service-desc" style="left:412px">Uncover many web sites still in their infancy various versions...</p>
  <p class="abs service-desc" style="left:562px">Uncover many web sites still in their infancy various versions...</p>

  <div class="abs pub-img" role="img" aria-label="Three business professionals standing together"></div>
  <h2 class="abs pub-title" style="font-weight:400">PUBLICATIONS</h2>
  <p class="abs pub-text">It is a long established fact that a reader will be distracted by the readable content of a page when looking at its layout. The point of using Lorem Ipsum is that it has a more-or-less normal distribution of letters, as opposed to using 'Content here, content here', making it look like readable English. Many desktop publishing packages and web page editors now use Lorem Ipsum as their default model text, and a search for 'lorem ipsum' will uncover many web sites still in their infancy. Various versions have evolved over the years...</p>
  <a class="abs btn"><span class="btn-label">READ MORE</span><span class="btn-arrow"><svg width="6" height="9" viewBox="0 0 6 9"><path d="M1 1 L5 4.5 L1 8" fill="none" stroke="#fff" stroke-width="1.3"/></svg></span></a>

  <section class="abs posts">
    <h2 class="section-title">RECENT POSTS</h2>
    <svg class="abs posts-arrow" style="left:79px" width="6" height="14" viewBox="0 0 6 14"><path d="M5 1 L1 7 L5 13" fill="none" stroke="#8fd6bd" stroke-width="1"/></svg>
    <svg class="abs posts-arrow" style="left:725px" width="6" height="14" viewBox="0 0 6 14"><path d="M1 1 L5 7 L1 13" fill="none" stroke="#8fd6bd" stroke-width="1"/></svg>
    <div class="abs post-img" style="left:116px;background:linear-gradient(135deg,#f2f2f2,#c9c3be)" role="img" aria-label="Three colleagues reviewing documents"></div>
    <div class="abs post-img" style="left:315px;background:linear-gradient(135deg,#2a2a2a,#d8c8b8 55%,#2a2a2a)" role="img" aria-label="Business handshake over a desk"></div>
    <div class="abs post-img" style="left:516px;background:linear-gradient(135deg,#dcdad6,#8a8884)" role="img" aria-label="Two colleagues working at a laptop"></div>
    <div class="abs post-title" style="left:116px">It is a long established fact reader</div>
    <div class="abs post-title" style="left:315px">It is a long established fact reader</div>
    <div class="abs post-title" style="left:516px">It is a long established fact reader</div>
    <div class="abs post-date" style="left:116px">Posted on 27 march 2014</div>
    <div class="abs post-date" style="left:315px">Posted on 27 march 2014</div>
    <div class="abs post-date" style="left:516px">Posted on 27 march 2014</div>
  </section>

  <footer class="abs footer">
    <ul class="abs footer-nav">
      <li style="width:50px">Home</li><li style="width:49px">About</li><li style="width:57px">Services</li><li style="width:54px">Contact</li><li style="width:68px">Publications</li><li style="width:45px">Blog</li><li>Links</li>
    </ul>
    <p class="abs copy">Copyrights © 2014. Whitford Research. All Rights Reserved</p>
    <div class="abs social"><span></span><span></span><span></span><span></span></div>
  </footer>
</div>
</body>
</html>
```